Law Firm Stationery Design - Traditional Meets Intuitive

Looking for a modern, yet classic, law firm stationery design. Simplicity is desired, but great ideas are encouraged. See attachment for company information. We utilize a variety of non-traditional legal tools to bring a different perspective to each of our client's particular situation. Final design should communicate classic values with intuitive, unique solutions.

Industry/Entity Type

Law Firm

Requirements
Should not have
• - No typical legal icons
• - No Tag Line!
• - DO NOT WANT WHAT WE ALREADY HAVE

```html
<!DOCTYPE html>
<html lang="en">
<head>
<meta charset="utf-8">
<title>Lumera Law LLC Letterhead</title>
<link href="https://fonts.googleapis.com/css2?family=Arimo:wght@400&family=Questrial&display=swap" rel="stylesheet">
<style>
  :root {
    --backdrop: #cfe3bd;
    --paper: #ffffff;
    --paper-tint: #eef5e6;
    --lime: #8cc125;
    --lime-soft: #a9cf5b;
    --ink: #1d1d1d;
    --muted: #8a8a8a;
    --steel: #a9abb0;
    --signature-tone: #eef0ea;
  }
  * { margin: 0; padding: 0; box-sizing: border-box; }
  html, body { width: 1200px; height: 784px; overflow: hidden; }
  body {
    background: var(--backdrop);
    display: flex;
    align-items: center;
    justify-content: center;
    font-family: "Arimo", Arial, sans-serif;
  }
  .letterhead {
    position: relative;
    width: 572px;
    height: 740px;
    background: linear-gradient(35deg, var(--paper-tint) 0%, var(--paper) 45%);
    box-shadow: 0 6px 18px rgba(60, 90, 30, 0.18);
    overflow: hidden;
  }
  .corner-bar {
    position: absolute;
    top: 14px;
    height: 5px;
    background: var(--steel);
  }
  .corner-bar--left { left: 0; width: 42px; }
  .corner-bar--right { right: 0; width: 38px; }
  .sender {
    position: absolute;
    top: 28px;
    left: 58px;
    font-family: "Questrial", sans-serif;
  }
  .sender__name { color: var(--lime); font-size: 11px; letter-spacing: 0.3px; }
  .sender__role { color: var(--muted); font-size: 7.5px; margin-top: 1px; }
  .header-rule {
    position: absolute;
    top: 52px;
    left: 120px;
    width: 232px;
    height: 3px;
    background: var(--lime);
  }
  .contact {
    position: absolute;
    top: 38px;
    left: 364px;
    font-size: 7px;
    font-style: normal;
    color: var(--muted);
    line-height: 1.5;
  }
  .contact__row { display: flex; align-items: center; gap: 3px; white-space: nowrap; }
  .contact__row svg { width: 7px; height: 7px; flex: none; }
  .contact__gap { margin-left: 6px; display: inline-flex; align-items: center; gap: 3px; }
  .firm-name {
    position: absolute;
    top: 44px;
    left: 38px;
    list-style: none;
    font-family: "Questrial", sans-serif;
    font-size: 26px;
    color: var(--lime-soft);
    line-height: 57px;
    text-align: center;
    width: 26px;
  }
  .letter-body {
    position: absolute;
    top: 96px;
    left: 150px;
    width: 372px;
    font-size: 10.4px;
    line-height: 1.32;
    color: var(--ink);
  }
  .letter-body p { margin-bottom: 13px; text-indent: 24px; }
  .signature {
    position: absolute;
    top: 540px;
    left: 244px;
    width: 150px;
    height: 44px;
    background: linear-gradient(90deg, var(--paper), var(--signature-tone));
    border-radius: 3px;
  }
  .footer-band {
    position: absolute;
    left: 0; right: 0; bottom: 0;
    height: 8px;
    background: var(--lime);
  }
</style>
</head>
<body>
  <main class="letterhead">
    <div class="corner-bar corner-bar--left"></div>
    <div class="corner-bar corner-bar--right"></div>

    <header>
      <div class="sender">
        <div class="sender__name">Example Name</div>
        <div class="sender__role">Trainee Designation</div>
      </div>
      <div class="header-rule"></div>
      <address class="contact">
        <div class="contact__row">
          <svg viewBox="0 0 10 10"><circle cx="5" cy="5" r="5" fill="#8cc125"/><circle cx="5" cy="4.3" r="1.6" fill="#fff"/></svg>
          18 Harbor Lane, Suite 300 Fairview, MA 02000
        </div>
        <div class="contact__row">
          <svg viewBox="0 0 10 10"><circle cx="5" cy="5" r="5" fill="#8cc125"/><rect x="3.6" y="2.4" width="2.8" height="5.2" rx="0.6" fill="#fff"/></svg>
          555-014-2200
          <span class="contact__gap">
            <svg viewBox="0 0 10 10"><circle cx="5" cy="5" r="5" fill="#8cc125"/><circle cx="5" cy="5" r="2.6" fill="none" stroke="#fff" stroke-width="0.9"/></svg>
            www.lumeralaw.com
          </span>
        </div>
      </address>
    </header>

    <ul class="firm-name" aria-label="Lumera Law LLC">
      <li>L</li><li>U</li><li>M</li><li>E</li><li>R</li><li>A</li>
      <li>L</li><li>A</li><li>W</li><li>L</li><li>L</li><li>C</li>
    </ul>

    <section class="letter-body">
      <p>Lorem Ipsum is simply dummy text of the printing and typesetting industry. Lorem Ipsum has been the industry's standard dummy text ever since the 1500s, when an unknown printer took a galley of type and scrambled it to make a type specimen book. It has survived not only five centuries, but also the leap into electronic typesetting, remaining essentially unchanged. It was popularised in the 1960s with the release of Lettrafold sheets containing Lorem Ipsum passages, and more recently with desktop publishing software like Folio PageSet including versions of Lorem Ipsum.</p>
      <p>It is a long established fact that a reader will be distracted by the readable content of a page when looking at its layout. The point of using Lorem Ipsum is that it has a more-or-less normal distribution of letters, as opposed to using 'Content here, content here', making it look like readable English. Many desktop publishing packages and web page editors now use Lorem Ipsum as their default model text, and a search for 'lorem ipsum' will uncover many web sites still in their infancy. Various versions have evolved over the years, sometimes by accident, sometimes on purpose (injected humour and the like).</p>
      <p>Contrary to popular belief, Lorem Ipsum is not simply random text. It has roots in a piece of classical Latin literature from 45 BC, making it over 2000 years old. Daniel Varrow, a Latin professor at Eastbrook College in Westmere, looked up one of the more obscure Latin words, consectetur, from a Lorem Ipsum passage, and going through the cites of the word in classical literature, discovered the undoubtable source. Lorem Ipsum comes from sections 1.10.32 and 1.10.33 of "de Natura Verborum et Sonorum" structures, to generate Lorem Ipsum which looks reasonable. The generated Lorem Ipsum is therefore always free from repetition, injected humour, or non-characteristic words etc.</p>
    </section>

    <div class="signature" role="img" aria-label="Handwritten signature of the letter's sender"></div>

    <div class="footer-band"></div>
  </main>
</body>
</html>
```